Bright Meadow Counseling Business Card design with a visually interesting use of Space

I need business cards that are luxurious and give a peaceful, calm vibe. I also had some letterhead designed, and i like the look of it also, it's attached with the logo design for reference/ ideas but feel free to be creative.

Target Market(s)

High end luxurious client who needs counseling

Industry/Entity Type

Marriage and Family Therapy

Contact Information for Business Card

Mira Kowalczyk MS LMFT/ or Toby Hallett address 4150 Larkin Suite 600

Font styles to use
Sans Serif

Colors
0054AA
0677BA
7BADD7
CADEEF
E8F1F8
0094D4
00A9DD
6FCCEA
C7EBF8
E9F6FB
A7469A
B969AE
D3A5CF
EDDBEB
F8F0F9
6B429C
8869AF
B7A5CE
E3DAEB
F3F0F8

Requirements
Must have
• Logo and color scheme but be simple modern and luxurious
Nice to have
• I'd like to incorporate some elelmets from the logo and letterhead into a simple modern card

```html
<!DOCTYPE html>
<html lang="en">
<head>
<meta charset="utf-8">
<title>Bright Meadow Counseling – Business Card</title>
<link rel="stylesheet" href="https://fonts.googleapis.com/css2?family=Raleway:wght@200&family=Arimo:wght@400;700&display=swap">
<style>
  :root {
    --backdrop: #ecedee;
    --card: #323232;
    --white: #ffffff;
    --teal: #5cc6bf;
    --text: #e6e6e6;
    --purple: #b969ae;
    --violet: #8869af;
    --sky: #6fccea;
  }
  * { box-sizing: border-box; margin: 0; padding: 0; }
  html, body { width: 1200px; height: 802px; overflow: hidden; }
  body {
    background: var(--backdrop);
    position: relative;
    font-family: "Arimo", Arial, sans-serif;
  }
  .card {
    position: absolute;
    top: 246px;
    width: 540px;
    height: 309px;
    background: var(--card);
    box-shadow: 0 6px 18px rgba(0,0,0,0.18);
    overflow: hidden;
  }
  .card--front { left: 40px; }
  .card--back { left: 620px; }

  .brand {
    font-family: "Raleway", Helvetica, sans-serif;
    font-weight: 200;
    color: var(--white);
    line-height: 1.05;
    letter-spacing: 0.02em;
  }
  .card--front .brand {
    position: absolute;
    left: 34px;
    top: 40px;
    font-size: 27px;
  }
  .card--back .brand {
    position: absolute;
    left: 0;
    right: 0;
    top: 150px;
    text-align: center;
    font-size: 40px;
  }
  .brand-dot {
    position: absolute;
    border-radius: 50%;
  }
  .card--back .brand-dot {
    width: 58px; height: 58px;
    left: 241px; top: 70px;
    background: var(--violet);
  }
  .feature-circle {
    position: absolute;
    right: 46px;
    top: 58px;
    width: 190px;
    height: 190px;
    border-radius: 50%;
    background: radial-gradient(circle at 35% 35%, var(--sky), var(--violet) 55%, var(--purple));
    opacity: 0.9;
  }

  .contact {
    position: absolute;
    left: 34px;
    top: 132px;
    color: var(--text);
    font-size: 13px;
    line-height: 1.3;
  }
  .contact__name {
    color: var(--teal);
    font-weight: 700;
    font-size: 17px;
    letter-spacing: 0.01em;
  }
  .contact__title { margin-bottom: 10px; }
  .contact__address { margin-bottom: 10px; }
  .contact__line {
    display: flex;
    align-items: center;
    gap: 7px;
  }
  .contact__line svg { width: 11px; height: 11px; flex: none; }
</style>
</head>
<body>

<section class="card card--front" aria-label="Business card front">
  <div class="brand">Bright Meadow<br>Counseling</div>
  <div class="feature-circle"></div>

  <div class="contact">
    <div class="contact__name">MIRA KOWALCZYK</div>
    <div class="contact__title">MS LMFT</div>
    <div class="contact__address">2210 willow bend lane<br>fairbanks, alaska 99701</div>

    <div class="contact__line">
      <svg viewBox="0 0 12 12" aria-hidden="true"><path fill="var(--teal)" d="M2.5 1 4.5 3.2 3.6 4.5c.7 1.6 2.1 3 3.8 3.8l1.3-.9L11 9.5 9.6 11C5 10.6 1.4 7 1 2.4Z"/></svg>
      <span>555-214-7730</span>
    </div>
    <div class="contact__line">
      <svg viewBox="0 0 12 12" aria-hidden="true"><rect x="3" y="1" width="6" height="3" fill="var(--teal)"/><rect x="1" y="4.5" width="10" height="4.5" rx="1" fill="var(--teal)"/><rect x="3" y="8" width="6" height="3" fill="var(--teal)"/></svg>
      <span>555-318-4062</span>
    </div>
    <div class="contact__line">
      <svg viewBox="0 0 12 12" aria-hidden="true"><rect x="1" y="2.5" width="10" height="7" fill="var(--teal)"/><path d="M1 2.5 6 6.5 11 2.5" fill="none" stroke="var(--card)" stroke-width="1"/></svg>
      <span>info@brightmeadow.com</span>
    </div>
    <div class="contact__line">
      <svg viewBox="0 0 12 12" aria-hidden="true"><circle cx="6" cy="6" r="5" fill="var(--teal)"/><path d="M1 6h10M6 1c-2.5 2.8-2.5 7.2 0 10M6 1c2.5 2.8 2.5 7.2 0 10" fill="none" stroke="var(--card)" stroke-width="0.8"/></svg>
      <span>www.brightmeadow.com</span>
    </div>
  </div>
</section>

<section class="card card--back" aria-label="Business card back">
  <div class="brand-dot"></div>
  <div class="brand">Bright Meadow<br>Counseling</div>
</section>

</body>
</html>
```